Upscale Adult website

Looking for the design mock-up of an intuitive, professional and upscale adult website. No HTML necessary, just a competent design theme. The site will be category centric. This means that finding and selecting a specific categories in any easy and intuitive way is vey important. Looking for mock-up of Home Page, a Category Screen, and the Login Screen. The site should have a fun feel but be more corporate rather than "porn." There must also be free space where ads will appear. See attached file for complete list of functionality and necessary icons for the Home Screen.

```html
<!DOCTYPE html>
<html lang="en">
<head>
<meta charset="utf-8">
<title>Video Portal Home</title>
<link href="https://fonts.googleapis.com/css2?family=Catamaran:wght@400;500;600&display=swap" rel="stylesheet">
<style>
:root{
  --bg:#2b2b2b;
  --bg-dark:#1c1c1c;
  --panel:#0b0b0b;
  --panel-edge:#1a1a1a;
  --text:#ffffff;
  --muted:#a9a9a9;
  --dim:#6b6b6b;
  --red:#e3202a;
  --frame:#4a4a4a;
}
*{box-sizing:border-box;margin:0;padding:0}
html,body{width:1200px;height:797px;overflow:hidden}
body{
  position:relative;
  background:radial-gradient(ellipse at 50% 40%,#3a3a3a 0%,var(--bg) 55%,var(--bg-dark) 100%);
  font-family:"Catamaran",sans-serif;color:var(--text);
}
.abs{position:absolute}
.topbar{left:133px;top:0;width:934px;height:45px;background:linear-gradient(#2a2a2a,#111);}
.nav-item{top:14px;font-size:16px;font-weight:500;color:var(--muted);letter-spacing:.3px}
.nav-caret{left:676px;top:33px;width:0;height:0;border-left:5px solid transparent;border-right:5px solid transparent;border-top:7px solid var(--muted)}
.round-icon{top:11px;width:25px;height:25px}
.field{top:11px;height:18px;border-radius:9px;background:#000;border:1px solid #333;font-size:11px;color:var(--dim);padding:0 11px;line-height:17px}
.register{left:960px;top:30px;font-size:9px;color:var(--muted)}
.register u{text-decoration:underline}
.logo-panel{left:133px;top:45px;width:174px;height:84px;background:linear-gradient(#141414,#050505);border-radius:0 0 10px 10px;}
.logo-text{left:154px;top:76px;font-size:16px;font-weight:500}
.cat-strip{left:307px;top:45px;width:760px;height:75px;background:#050505}
.cat-thumb{top:52px;width:61px;height:60px;background:linear-gradient(160deg,#9a8b80,#d9d3cf);border:1px solid #222}
.cat-thumb.dark{background:linear-gradient(160deg,#2b2b2b,#050505)}
.cat-thumb span{position:absolute;left:0;right:0;bottom:0;height:24px;background:rgba(200,200,200,.8);color:#111;font-size:7.5px;font-weight:600;text-align:center;line-height:9px;display:flex;align-items:center;justify-content:center}
.featured-band{left:165px;top:153px;width:870px;height:217px;background:linear-gradient(90deg,rgba(0,0,0,0),#000 8%,#000 92%,rgba(0,0,0,0))}
.section-title{font-size:16px;font-weight:500}
.video{width:151px;height:151px;border:2px solid var(--frame);background:linear-gradient(160deg,#8c7c70,#d6d0cc)}
.video.dark{background:linear-gradient(160deg,#333,#050505)}
.video.blue{background:linear-gradient(170deg,#9db7da,#c9a77c 60%,#2a2a2a)}
.video.light{background:linear-gradient(160deg,#cfc9c5,#9c8a7d)}
.video svg{position:absolute;left:61px;top:56px}
.play-label{position:absolute;left:0;right:0;top:122px;text-align:center;color:var(--red);font-size:15px;font-weight:600}
.recent-panel{left:133px;top:398px;width:934px;height:420px;background:linear-gradient(#111,#000 30px);border-radius:10px 10px 0 0}
.video-title{width:160px;font-size:14.5px;line-height:19px;color:var(--red);font-weight:500}
.video-meta{width:161px;font-size:14px;color:var(--dim);display:flex;justify-content:space-between;align-items:center}
.likes{display:flex;align-items:center;gap:3px}
.arrow{width:24px;height:38px}
</style>
</head>
<body>

<div class="abs topbar"></div>
<nav>
  <div class="abs nav-item" style="left:154px">HOME</div>
  <div class="abs nav-item" style="left:232px">HIGHEST RATED</div>
  <div class="abs nav-item" style="left:375px">MOST VIEWED</div>
  <div class="abs nav-item" style="left:492px">RECENTLY ADDED</div>
  <div class="abs nav-item" style="left:639px">CATEGORIES</div>
  <div class="abs nav-caret"></div>
</nav>
<svg class="abs round-icon" style="left:750px" viewBox="0 0 25 25" aria-label="Favourites"><circle cx="12.5" cy="12.5" r="11" fill="none" stroke="#a9a9a9" stroke-width="2"/><path d="M12.5 18 L7 12.5 A3 3 0 0 1 12.5 8.5 A3 3 0 0 1 18 12.5 Z" fill="#a9a9a9"/></svg>
<svg class="abs round-icon" style="left:786px" viewBox="0 0 25 25" aria-label="Upload"><circle cx="12.5" cy="12.5" r="11" fill="none" stroke="#a9a9a9" stroke-width="2"/><path d="M12.5 6 L8 11 H11 V16 H14 V11 H17 Z M8 18 H17" fill="#a9a9a9" stroke="#a9a9a9" stroke-width="1.2"/></svg>
<div class="abs field" style="left:831px;width:91px">name</div>
<div class="abs field" style="left:936px;width:92px">password<span style="float:right;color:#aaa">&gt;</span></div>
<div class="abs register">or <u>register</u></div>

<div class="abs logo-panel"></div>
<div class="abs logo-text">PLACE LOGO HERE</div>

<div class="abs cat-strip"></div>
<div class="abs cat-thumb" style="left:317px" role="img" aria-label="Category preview"><span>ASIAN</span></div>
<div class="abs cat-thumb dark" style="left:382px" role="img" aria-label="Category preview"><span>GIRL ON<br>GIRL</span></div>
<div class="abs cat-thumb light" style="left:447px" role="img" aria-label="Category preview"><span>TWO ON<br>ONE</span></div>
<div class="abs cat-thumb" style="left:513px;background:linear-gradient(170deg,#9db7da,#c9a77c)" role="img" aria-label="Category preview"><span>LATINA</span></div>
<div class="abs cat-thumb" style="left:579px" role="img" aria-label="Category preview"><span>MASTURBA-<br>TION</span></div>
<div class="abs cat-thumb dark" style="left:644px" role="img" aria-label="Category preview"><span>FOOT<br>FETISH</span></div>
<div class="abs cat-thumb light" style="left:710px" role="img" aria-label="Category preview"><span>LATINA</span></div>
<div class="abs cat-thumb" style="left:775px;background:linear-gradient(170deg,#9db7da,#c9a77c)" role="img" aria-label="Category preview"><span>ASIAN</span></div>
<div class="abs cat-thumb" style="left:841px" role="img" aria-label="Category preview"><span>ASIAN</span></div>
<div class="abs cat-thumb dark" style="left:906px" role="img" aria-label="Category preview"><span>ASIAN</span></div>
<div class="abs cat-thumb light" style="left:971px" role="img" aria-label="Category preview"><span>ASIAN</span></div>
<svg class="abs" style="left:1044px;top:72px" width="12" height="20" viewBox="0 0 12 20"><path d="M1 1 L11 10 L1 19 Z" fill="#bbb"/></svg>

<div class="abs featured-band"></div>
<div class="abs section-title" style="left:193px;top:165px">FEATURED VIDEOS/ADS</div>
<svg class="abs arrow" style="left:148px;top:263px" viewBox="0 0 24 38"><path d="M22 2 L4 19 L22 36 Z" fill="#777"/></svg>
<svg class="abs arrow" style="left:1025px;top:263px" viewBox="0 0 24 38"><path d="M2 2 L20 19 L2 36 Z" fill="#777"/></svg>

<div class="abs video" style="left:193px;top:201px" role="img" aria-label="Featured video still"><svg width="30" height="36" viewBox="0 0 30 36"><path d="M2 2 L28 18 L2 34 Z" fill="#fff"/></svg></div>
<div class="abs video dark" style="left:357px;top:201px" role="img" aria-label="Featured video still"><svg width="30" height="36" viewBox="0 0 30 36"><path d="M2 2 L28 18 L2 34 Z" fill="#fff"/></svg></div>
<div class="abs video light" style="left:522px;top:201px" role="img" aria-label="Featured video still"><svg width="30" height="36" viewBox="0 0 30 36"><path d="M2 2 L28 18 L2 34 Z" fill="#fff"/></svg></div>
<div class="abs video blue" style="left:688px;top:201px" role="img" aria-label="Featured video still, hovered"><svg width="30" height="36" viewBox="0 0 30 36"><path d="M2 2 L28 18 L2 34 Z" fill="#e3202a"/></svg><div class="play-label">PLAY VIDEO</div></div>
<div class="abs video" style="left:855px;top:201px" role="img" aria-label="Featured video still"><svg width="30" height="36" viewBox="0 0 30 36"><path d="M2 2 L28 18 L2 34 Z" fill="#fff"/></svg></div>

<div class="abs recent-panel"></div>
<div class="abs section-title" style="left:193px;top:413px">RECENTLY ADDED VIDEOS</div>

<div class="abs video" style="left:193px;top:452px" role="img" aria-label="Video still"><svg width="30" height="36" viewBox="0 0 30 36"><path d="M2 2 L28 18 L2 34 Z" fill="#fff"/></svg></div>
<div class="abs video dark" style="left:357px;top:452px" role="img" aria-label="Video still"><svg width="30" height="36" viewBox="0 0 30 36"><path d="M2 2 L28 18 L2 34 Z" fill="#fff"/></svg></div>
<div class="abs video light" style="left:522px;top:452px" role="img" aria-label="Video still"><svg width="30" height="36" viewBox="0 0 30 36"><path d="M2 2 L28 18 L2 34 Z" fill="#fff"/></svg></div>
<div class="abs video blue" style="left:688px;top:452px" role="img" aria-label="Video still"><svg width="30" height="36" viewBox="0 0 30 36"><path d="M2 2 L28 18 L2 34 Z" fill="#fff"/></svg></div>
<div class="abs video" style="left:855px;top:452px" role="img" aria-label="Video still"><svg width="30" height="36" viewBox="0 0 30 36"><path d="M2 2 L28 18 L2 34 Z" fill="#fff"/></svg></div>

<div class="abs video-title" style="left:193px;top:612px">Title of the video first and second line...</div>
<div class="abs video-title" style="left:357px;top:612px">Title of the video first and second line...</div>
<div class="abs video-title" style="left:522px;top:612px">Title of the video first and second line...</div>
<div class="abs video-title" style="left:688px;top:612px">Title of the video first and second line...</div>
<div class="abs video-title" style="left:855px;top:612px">Title of the video first and second line...</div>

<div class="abs video-meta" style="left:193px;top:650px"><span>200 views</span><span class="likes"><svg width="15" height="15" viewBox="0 0 15 15"><circle cx="7.5" cy="7.5" r="6.5" fill="none" stroke="#e3202a" stroke-width="1.3"/><path d="M7.5 11 L4 7.5 A2 2 0 0 1 7.5 5 A2 2 0 0 1 11 7.5 Z" fill="#e3202a"/></svg>&nbsp;&nbsp;15</span></div>
<div class="abs video-meta" style="left:357px;top:650px"><span>5.003 views</span><span class="likes"><svg width="15" height="15" viewBox="0 0 15 15"><circle cx="7.5" cy="7.5" r="6.5" fill="none" stroke="#e3202a" stroke-width="1.3"/><path d="M7.5 11 L4 7.5 A2 2 0 0 1 7.5 5 A2 2 0 0 1 11 7.5 Z" fill="#e3202a"/></svg>243</span></div>
<div class="abs video-meta" style="left:522px;top:650px"><span>1.233 views</span><span class="likes"><svg width="15" height="15" viewBox="0 0 15 15"><circle cx="7.5" cy="7.5" r="6.5" fill="none" stroke="#e3202a" stroke-width="1.3"/><path d="M7.5 11 L4 7.5 A2 2 0 0 1 7.5 5 A2 2 0 0 1 11 7.5 Z" fill="#e3202a"/></svg>175</span></div>
<div class="abs video-meta" style="left:688px;top:650px"><span>1.233.989 views</span><span class="likes"><svg width="15" height="15" viewBox="0 0 15 15"><circle cx="7.5" cy="7.5" r="6.5" fill="none" stroke="#e3202a" stroke-width="1.3"/><path d="M7.5 11 L4 7.5 A2 2 0 0 1 7.5 5 A2 2 0 0 1 11 7.5 Z" fill="#e3202a"/></svg>243</span></div>
<div class="abs video-meta" style="left:855px;top:650px"><span>33.989 views</span><span class="likes"><svg width="15" height="15" viewBox="0 0 15 15"><circle cx="7.5" cy="7.5" r="6.5" fill="none" stroke="#e3202a" stroke-width="1.3"/><path d="M7.5 11 L4 7.5 A2 2 0 0 1 7.5 5 A2 2 0 0 1 11 7.5 Z" fill="#e3202a"/></svg>175</span></div>

<div class="abs video" style="left:193px;top:684px" role="img" aria-label="Video still"><svg width="30" height="36" viewBox="0 0 30 36"><path d="M2 2 L28 18 L2 34 Z" fill="#fff"/></svg></div>
<div class="abs video dark" style="left:357px;top:684px" role="img" aria-label="Video still"><svg width="30" height="36" viewBox="0 0 30 36"><path d="M2 2 L28 18 L2 34 Z" fill="#fff"/></svg></div>
<div class="abs video light" style="left:522px;top:684px" role="img" aria-label="Video still"><svg width="30" height="36" viewBox="0 0 30 36"><path d="M2 2 L28 18 L2 34 Z" fill="#fff"/></svg></div>
<div class="abs video blue" style="left:688px;top:684px" role="img" aria-label="Video still"><svg width="30" height="36" viewBox="0 0 30 36"><path d="M2 2 L28 18 L2 34 Z" fill="#fff"/></svg></div>
<div class="abs video" style="left:855px;top:684px" role="img" aria-label="Video still"><svg width="30" height="36" viewBox="0 0 30 36"><path d="M2 2 L28 18 L2 34 Z" fill="#fff"/></svg></div>

</body>
</html>
```